Fence Contractor Website Design

We are working with Yardline Works. They are a local fencing and automatic gate installer and in need of a new website design.
Some sites to use for inspiration:
https://pinevalebarrier.example
https://marwickrails.example
https://www.tellurpostsandboards.example
https://www.grovanpaneling.example
Thank you for taking the time to consider designing a website for us. We are web developers based in Stockton, CA, USA. Most of our projects go through the same process. Understanding this process may help you win a project with us. We custom-code all of our websites in-house. We don’t have any requirements as to what tools you use for your design, but we prefer Figma files. For any design that we label as four-stars, we send it to the client for review. The client picks the final design they want us to use. Once we complete this process, we will continue to show additional clients all the four-star sites and purchase them later. Your designs will have multiple chances to sell. For better chances of success, we ask that you follow these guidelines.
IMAGES:
If you use any images or icons in the design, we ask that you have a link to the asset so we can purchase the image/icon. Most of the designs we submit do not have the customer’s images on them unless they have some great images. Be creative; show us the feeling you are trying to portray with your image choices. Use any royalty-free site you choose. We subscribe to Stockvane and mainly use their images, but we can purchase images outside of Stockvane.
PLEASE NOTE: we will not submit designs to clients with watermarks on the images.
FONTS:
We ask that you identify the fonts used in the design. This can be done in a message if you want. We typically use Google Fonts and Stockvane Fonts.
CONTENT:
We're always open to different content and ideas. We often submit designs with stock images so the client can see our vision. We typically take pictures after the website launch to use their images with our vision. Lorem Ipsum is fine for paragraphs, but we ask that you write the headers in correct English. We want to be able to show the vision and identify the sections of the website.
INSPIRATION:
We typically add a couple of links in the brief of websites we like to help you get started in your design.
REVISIONS:
We do not often ask for revisions of the designs unless we see something in the design that may not appeal to the client. If there are slight changes that we want to make, we do that in the development process.
FEEDBACK:
We rarely give feedback on designs during the design process. We are working on many website projects and do not have the time to provide feedback. We usually respond if your request is well thought out and asks specific questions, but a note asking “feedback, please” usually goes unanswered.
Number of Pages Required
1 page
Look and feel
Each slider illustrates characteristics of the customer's brand and the style your logo design should communicate.

```html
<!DOCTYPE html>
<html lang="en">
<head>
<meta charset="utf-8">
<title>Yardline Works — Fences &amp; Automated Gates</title>
<link rel="stylesheet" href="https://fonts.googleapis.com/css2?family=Poppins:wght@300;400;500;600;700&display=swap">
<style>
:root{
  --navy:#0d2a6b;
  --navy-deep:#0a2259;
  --red:#e3161f;
  --ink:#1d2333;
  --muted:#5a6072;
  --line:#d9dde6;
  --soft:#f3f5fa;
  --white:#ffffff;
}
*{box-sizing:border-box;margin:0;padding:0}
html,body{width:1200px;height:4622px;overflow:hidden}
body{font-family:"Poppins",sans-serif;color:var(--ink);background:var(--white);position:relative}
section,header,footer{position:relative;width:1200px}
ul{list-style:none}
a{color:inherit;text-decoration:none}

/* buttons */
.btn{position:absolute;display:flex;align-items:center;justify-content:center;gap:7px;border-radius:6px;font-weight:600;font-size:13px;height:37px;padding:0 12px;white-space:nowrap}
.btn svg{width:17px;height:17px;flex:none}
.btn-red{background:var(--red);color:var(--white)}
.btn-navy{background:var(--navy);color:var(--white)}
.btn-ghost{border:1.5px solid var(--white);color:var(--white);background:transparent}
.btn-phone{font-size:14px}

/* tick list */
.ticks li{position:relative;padding-left:21px;font-size:14px;color:#3b4152;line-height:1}
.ticks li::before{content:"";position:absolute;left:0;top:0;width:13px;height:13px;border-radius:50%;background:var(--red)}
.ticks li::after{content:"";position:absolute;left:4px;top:3px;width:3px;height:5px;border:solid var(--white);border-width:0 1.6px 1.6px 0;transform:rotate(45deg)}
.ticks.on-navy li{color:var(--white);font-size:13px}

.photo{position:absolute}
.accent-bar{position:absolute;width:3px;background:var(--red)}

/* header */
.site-header{height:93px;background:var(--white)}
.brand{position:absolute;left:167px;top:35px;display:flex;align-items:center;gap:8px;font-weight:700;font-size:17px;color:var(--navy)}
.brand i{display:block;width:14px;height:14px;background:var(--red)}
.nav{position:absolute;top:38px;left:400px;font-size:13px;color:#2b3040}
.nav a{position:absolute;white-space:nowrap}
.header-call{position:absolute;left:832px;top:27px;height:36px;width:152px;display:flex;align-items:center}
.header-call svg{width:24px;height:24px;color:var(--navy);flex:none}
.header-call .pill{margin-left:6px;background:var(--red);color:var(--white);border-radius:18px;height:36px;flex:1;padding:5px 8px 0 9px;line-height:1;white-space:nowrap}
.header-call small{display:block;font-size:7.5px;font-weight:600;margin-bottom:2px}
.header-call b{display:block;font-size:13px;font-weight:600}
.header-quote{left:992px;top:27px;width:154px;height:36px;border-radius:18px;font-size:12px}

/* hero */
.hero{height:506px}
.hero .photo{inset:0;background:linear-gradient(180deg,#8fa9d9 0%,#c7d3ea 40%,#e9edf2 62%,#7da24a 80%,#5d8a34 100%)}
.hero h1{position:absolute;left:161px;top:122px;font-size:45px;font-weight:700;line-height:45px;color:var(--navy-deep)}
.hero h2{position:absolute;left:161px;top:221px;font-size:28px;font-weight:600;line-height:36px;color:var(--navy-deep)}
.hero .btn-red{left:162px;top:325px;width:142px}
.hero .btn-navy{left:313px;top:325px;width:142px}

.quote-card{position:absolute;left:689px;top:101px;width:348px;height:524px;background:var(--white);border-radius:18px;box-shadow:0 4px 18px rgba(10,30,80,.18);z-index:3}
.quote-card .accent-bar{left:41px;top:24px;height:44px}
.quote-card .kicker{position:absolute;left:57px;top:26px;font-size:13px;font-weight:600;color:var(--navy)}
.quote-card h3{position:absolute;left:57px;top:44px;font-size:20px;font-weight:600;color:var(--navy);letter-spacing:.3px}
.field{position:absolute;left:27px;width:294px;height:37px;border:1px solid #e0e3ea;border-radius:4px;font-size:11px;color:#9aa0ad;padding:10px 14px;background:var(--white)}
.field.select{text-align:center}
.field.select::after{content:"";position:absolute;right:12px;top:13px;width:6px;height:6px;border:solid #9aa0ad;border-width:0 1.5px 1.5px 0;transform:rotate(45deg)}
.field.message{height:104px}
.quote-card .submit{left:27px;top:459px;width:294px;height:43px;border-radius:4px;font-size:13px}

/* call today */
.call-today{height:101px}
.call-today .accent-bar{left:167px;top:24px;height:63px;width:4px}
.call-today p{position:absolute;left:180px;top:17px;font-size:28px;font-weight:300;color:#6a6f7d;line-height:36px}
.call-today strong{position:absolute;left:180px;top:49px;font-size:36px;font-weight:400;color:var(--navy);line-height:40px}

/* welcome */
.welcome{height:674px}
.welcome h2{position:absolute;left:161px;top:62px;font-size:33px;font-weight:400;line-height:46px;color:var(--ink)}
.welcome .accent-bar{left:161px;top:226px;height:42px}
.welcome .lead{position:absolute;left:180px;top:223px;width:440px;font-size:14px;line-height:20px;color:#3b4152}
.welcome .body{position:absolute;left:180px;top:296px;width:450px;font-size:13.5px;line-height:20px;color:#5a6072}
.welcome .ticks{position:absolute;left:180px;top:426px;width:420px;display:grid;grid-template-columns:230px 190px;row-gap:17px}
.welcome .btn-red{left:180px;top:568px;width:140px}
.welcome .btn-navy{left:328px;top:568px;width:144px}
.welcome .ph-main{left:664px;top:61px;width:371px;height:258px;border-radius:16px;background:linear-gradient(160deg,#6f9c4a,#c9d6e0 45%,#e8a0b9 65%,#5d8a3a)}
.welcome .ph-a{left:664px;top:340px;width:181px;height:266px;border-radius:16px;background:linear-gradient(180deg,#3f6a32,#a8b8a0 55%,#f1f1ee 75%,#6c8e3f)}
.welcome .ph-b{left:863px;top:340px;width:181px;height:266px;border-radius:16px;background:linear-gradient(180deg,#4e7a38,#c2c9b8 50%,#f4f3ef 72%,#7a6a4a)}

/* why choose */
.why{height:542px}
.why .band{position:absolute;left:0;right:0;top:86px;bottom:0;background:var(--navy)}
.why .photo{left:161px;top:0;width:427px;height:542px;border-radius:16px 16px 0 0;background:linear-gradient(160deg,#3d6b2f,#d9728f 30%,#f3f2ee 55%,#6a8d4a)}
.why h2{position:absolute;left:632px;top:138px;font-size:32px;font-weight:400;color:var(--white);white-space:nowrap}
.why .accent-bar{left:632px;top:192px;height:60px}
.why .lead{position:absolute;left:647px;top:190px;width:380px;font-size:13px;line-height:20px;color:var(--white)}
.why .ticks{position:absolute;left:626px;top:268px;width:420px;display:grid;grid-template-columns:206px 210px;row-gap:14px}
.why .ticks li::after{display:none}
.why .ticks li::before{width:10px;height:10px;top:2px}
.why .note{position:absolute;left:626px;top:376px;width:400px;font-size:13px;line-height:20px;color:var(--white)}
.why .btn-red{left:626px;top:464px;width:106px;height:36px;font-size:12px}
.why .btn-ghost{left:741px;top:464px;width:145px;height:36px;font-size:12px}

/* services */
.services{height:513px}
.services h2{position:absolute;left:0;right:0;top:50px;text-align:center;font-size:36px;font-weight:400;color:var(--ink)}
.services .intro{position:absolute;left:205px;width:790px;top:113px;text-align:center;font-size:14px;line-height:22px;color:#5a6072}
.service-card{position:absolute;top:179px;width:196px;height:246px;background:var(--white);border-radius:10px;box-shadow:0 2px 12px rgba(10,30,80,.10);padding:8px}
.service-card .thumb{width:180px;height:194px;border-radius:10px}
.service-card h3{font-size:13px;font-weight:500;margin-top:12px;color:var(--ink)}
.slider-arrow{position:absolute;top:274px;width:28px;height:28px;border-radius:50%;background:var(--white);box-shadow:0 1px 6px rgba(0,0,0,.18)}
.slider-arrow::after{content:"";position:absolute;top:11px;width:6px;height:6px;border:solid #888;border-width:0 1.4px 1.4px 0}
.slider-arrow.prev{left:130px}
.slider-arrow.next{left:1043px}
.slider-arrow.prev::after{left:12px;transform:rotate(135deg)}
.slider-arrow.next::after{left:9px;transform:rotate(-45deg)}

/* build band */
.build{height:325px;background:linear-gradient(180deg,#1c3576,#233f82 50%,#1a3270)}
.build h2{position:absolute;left:0;right:0;top:60px;text-align:center;font-size:52px;font-weight:400;color:var(--white);letter-spacing:.5px}
.build p{position:absolute;left:180px;width:840px;top:136px;text-align:center;font-size:14px;line-height:21px;color:var(--white)}
.build .btn-red{left:455px;top:224px;width:138px}
.build .btn-ghost{left:604px;top:224px;width:143px}

/* areas */
.areas{height:635px}
.areas .photo{left:161px;top:68px;width:402px;height:459px;border-radius:18px;background:linear-gradient(160deg,#6e5a46,#f1ede4 35%,#e8e4da 65%,#8a8a84)}
.areas h2{position:absolute;left:601px;top:74px;font-size:36px;font-weight:400;line-height:46px;color:var(--ink)}
.areas .intro{position:absolute;left:601px;top:176px;width:420px;font-size:14px;line-height:23px;color:#5a6072}
.areas .ticks{position:absolute;left:601px;top:265px;width:380px;display:grid;grid-template-columns:207px 170px;row-gap:14px}
.areas .ticks li{font-size:13px}
.areas .outro{position:absolute;left:601px;top:412px;width:420px;font-size:14px;line-height:23px;color:#5a6072}
.areas .btn-red{left:601px;top:489px;width:140px}
.areas .btn-navy{left:749px;top:489px;width:144px}

/* testimonial */
.testimonial{height:325px;background:var(--navy)}
.testimonial .frame{position:absolute;left:161px;top:59px;width:878px;height:206px;border:1px solid rgba(255,255,255,.55)}
.testimonial .quote-mark{position:absolute;left:562px;top:29px;width:76px;height:46px;background:var(--navy);display:flex;justify-content:center}
.testimonial .stars{position:absolute;left:0;right:0;top:84px;display:flex;justify-content:center;gap:2px}
.testimonial .stars svg{width:16px;height:16px}
.testimonial blockquote{position:absolute;left:220px;width:760px;top:138px;text-align:center;font-size:15px;line-height:20px;color:var(--white)}
.testimonial cite{position:absolute;left:0;right:0;top:236px;text-align:center;font-style:normal;font-size:13px;font-weight:500;color:var(--white)}
.testimonial .role{position:absolute;left:0;right:0;top:256px;text-align:center;font-size:11px;color:var(--white)}
.t-arrow{position:absolute;top:162px;width:11px;height:11px;border:solid var(--white);border-width:0 2px 2px 0}
.t-arrow.prev{left:144px;transform:rotate(135deg)}
.t-arrow.next{left:1046px;transform:rotate(-45deg)}

/* faq */
.faq{height:421px;background:var(--soft)}
.faq h2{position:absolute;left:0;right:0;top:32px;text-align:center;font-size:36px;font-weight:400;color:var(--ink)}
.faq-item{position:absolute;width:380px;border-bottom:1px solid var(--line);font-size:13px;color:#3b4152;padding-bottom:14px}
.faq-item .q{display:flex;justify-content:space-between}
.faq-item .q span:last-child{font-size:15px;color:#555}
.faq-item .a{margin-top:18px;padding:0 4px;font-size:11.5px;line-height:19px;color:#5a6072}

/* footer */
.site-footer{height:487px;background:var(--navy)}
.cta-card{position:absolute;left:84px;top:0;width:1007px;height:140px;background:var(--white);border-radius:0 0 30px 30px}
.cta-card h2{position:absolute;left:77px;top:20px;font-size:37px;font-weight:400;line-height:44px;color:var(--ink)}
.cta-card .btn-red{left:664px;top:54px;width:140px}
.cta-card .btn-navy{left:813px;top:54px;width:142px}
.footer-brand{position:absolute;left:179px;top:220px;display:flex;align-items:center;gap:8px;font-weight:700;font-size:17px;color:var(--white)}
.footer-brand i{display:block;width:14px;height:14px;background:var(--red)}
.footer-about{position:absolute;left:170px;top:258px;width:300px;font-size:11.5px;line-height:18px;color:var(--white)}
.footer-col{position:absolute;top:221px;color:var(--white)}
.footer-col h4{font-size:14px;font-weight:600;margin-bottom:14px}
.footer-col li{font-size:13px;line-height:24px}
.contact li{display:flex;gap:10px;align-items:flex-start;line-height:22px;margin-bottom:6px}
.contact svg{width:14px;height:14px;margin-top:4px;flex:none;color:var(--white)}
.socials{position:absolute;left:884px;top:381px;display:flex;gap:6px}
.socials span{display:block;width:24px;height:24px;border-radius:50%;background:var(--white)}
.footer-rule{position:absolute;left:0;right:0;top:429px;border-top:1px solid rgba(255,255,255,.2)}
.copyright{position:absolute;left:168px;top:447px;font-size:12px;color:var(--white)}
</style>
</head>
<body>

<header class="site-header">
  <a class="brand" href="#"><i></i>Yardline Works</a>
  <nav class="nav">
    <a style="left:0">Home</a>
    <a style="left:63px">About us</a>
    <a style="left:157px">Services</a>
    <a style="left:241px">Gallery</a>
    <a style="left:319px">Contact us</a>
  </nav>
  <div class="header-call">
    <svg viewBox="0 0 24 24"><path fill="currentColor" d="M6.6 10.8a15 15 0 0 0 6.6 6.6l2.2-2.2a1 1 0 0 1 1-.25 11.4 11.4 0 0 0 3.6.6 1 1 0 0 1 1 1V20a1 1 0 0 1-1 1A17 17 0 0 1 3 4a1 1 0 0 1 1-1h3.5a1 1 0 0 1 1 1c0 1.25.2 2.45.6 3.6a1 1 0 0 1-.25 1z"/></svg>
    <div class="pill"><small>CALL US TODAY</small><b>555-014-2288</b></div>
  </div>
  <a class="btn btn-navy header-quote">GET A FREE QUOTE</a>
</header>

<section class="hero">
  <div class="photo" role="img" aria-label="Long white picket fence along a green lawn under a bright sky"></div>
  <h1>Where Strength<br>Meets Style —</h1>
  <h2>Elegant Fences &amp; Automated<br>Gates by Yardline Works</h2>
  <a class="btn btn-red btn-phone"><svg viewBox="0 0 24 24"><path fill="currentColor" d="M6.6 10.8a15 15 0 0 0 6.6 6.6l2.2-2.2a1 1 0 0 1 1-.25 11.4 11.4 0 0 0 3.6.6 1 1 0 0 1 1 1V20a1 1 0 0 1-1 1A17 17 0 0 1 3 4a1 1 0 0 1 1-1h3.5a1 1 0 0 1 1 1c0 1.25.2 2.45.6 3.6a1 1 0 0 1-.25 1z"/></svg>555-014-2288</a>
  <a class="btn btn-navy">GET A FREE QUOTE</a>

  <form class="quote-card">
    <span class="accent-bar"></span>
    <span class="kicker">looking for a Fence</span>
    <h3>GET A FREE ESTIMATE</h3>
    <div class="field" style="top:93px">First Name*</div>
    <div class="field" style="top:141px">Last Name*</div>
    <div class="field" style="top:190px">Phone*</div>
    <div class="field" style="top:238px">Email*</div>
    <div class="field select" style="top:287px">-------- Select Services --------</div>
    <div class="field message" style="top:335px">Message</div>
    <a class="btn btn-navy submit">GET A FREE QUOTE</a>
  </form>
</section>

<section class="call-today">
  <span class="accent-bar"></span>
  <p>Call Today For Service</p>
  <strong>555-014-2288</strong>
</section>

<section class="welcome">
  <h2>Welcome Home —<br>Fences &amp; Gates That Secure,<br>Beautify &amp; Last</h2>
  <span class="accent-bar"></span>
  <p class="lead">Various versions have evolved over the years, sometimes by accident, sometimes on purpose</p>
  <p class="body">The point of using Lorem Ipsum is that it has a more-or-less normal distribution of letters, as opposed to using 'Content here, content here', making it look like readable English. Many desktop publishing packages and web page editors now use Lorem Ipsum as their default model text,</p>
  <ul class="ticks">
    <li>Residential Fencing</li><li>Wood Fencing</li>
    <li>Commercial Fencing</li><li>Chain Link Fening</li>
    <li>Custom Decks</li><li>Iron Fencing</li>
    <li>Pergolas &amp; Patio Covers</li>
  </ul>
  <a class="btn btn-red btn-phone"><svg viewBox="0 0 24 24"><path fill="currentColor" d="M6.6 10.8a15 15 0 0 0 6.6 6.6l2.2-2.2a1 1 0 0 1 1-.25 11.4 11.4 0 0 0 3.6.6 1 1 0 0 1 1 1V20a1 1 0 0 1-1 1A17 17 0 0 1 3 4a1 1 0 0 1 1-1h3.5a1 1 0 0 1 1 1c0 1.25.2 2.45.6 3.6a1 1 0 0 1-.25 1z"/></svg>555-014-2288</a>
  <a class="btn btn-navy">GET A FREE QUOTE</a>
  <div class="photo ph-main" role="img" aria-label="House with flowering shrubs behind a white picket fence"></div>
  <div class="photo ph-a" role="img" aria-label="White picket gate set among trees"></div>
  <div class="photo ph-b" role="img" aria-label="Open white garden gate on a path"></div>
</section>

<section class="why">
  <div class="band"></div>
  <div class="photo" role="img" aria-label="White arched arbor gate framed by pink roses"></div>
  <h2>Why Choose Yardline Works?</h2>
  <span class="accent-bar"></span>
  <p class="lead">Many desktop publishing packages and web page editors now use Lorem Ipsum as their default model text, and a search for</p>
  <ul class="ticks on-navy">
    <li>Professional installation</li><li>Designed for beauty.</li>
    <li>Local service</li><li>Custom gates, tough fences</li>
    <li>Free on-site quotes</li><li>Strong protection.</li>
    <li>Built for safety</li><li>Smooth automation</li>
  </ul>
  <p class="note">Many desktop publishing packages and web page editors now use Lorem Ipsum as their default model text, and a search for</p>
  <a class="btn btn-red">READ MORE</a>
  <a class="btn btn-ghost">GET A FREE QUOTE</a>
</section>

<section class="services">
  <h2>Our Fence &amp; Deck Services</h2>
  <p class="intro">The point of using Lorem Ipsum is that it has a more-or-less normal distribution of letters, as opposed to using 'Content here, content here', making it look like readable</p>
  <span class="slider-arrow prev"></span>
  <article class="service-card" style="left:167px"><div class="thumb" role="img" aria-label="Yellow house behind a white picket fence" style="background:linear-gradient(180deg,#8db3e0,#e7d58e 45%,#d98aa0 70%,#f2f2f0)"></div><h3>Residential Fencing</h3></article>
  <article class="service-card" style="left:391px"><div class="thumb" role="img" aria-label="Black steel commercial gate" style="background:linear-gradient(180deg,#c9cdd2,#2a2d33 45%,#5a5e66 80%,#9fa3a8)"></div><h3>Commercial Fencing</h3></article>
  <article class="service-card" style="left:615px"><div class="thumb" role="img" aria-label="Wooden deck with white railing" style="background:linear-gradient(180deg,#a9b98a,#f0ede6 45%,#c8894e 70%,#a56a38)"></div><h3>Custom Decks</h3></article>
  <article class="service-card" style="left:838px"><div class="thumb" role="img" aria-label="Pergola over a patio seating area" style="background:linear-gradient(180deg,#7a5a44,#c8b79a 40%,#8ca36b 70%,#6f6a5e)"></div><h3>Pergolas &amp; Patio Covers</h3></article>
  <span class="slider-arrow next"></span>
</section>

<section class="build" role="img" aria-label="Blue-toned view of a white fence line behind the banner text">
  <h2>BUILD YOUR FENCE TODAY!</h2>
  <p>The point of using Lorem Ipsum is that it has a more-or-less normal distribution of letters, as opposed to using 'Content here, content here', making it look like readable English. Many desktop publishing packages and web page editors now use Lorem Ipsum as their default model text.</p>
  <a class="btn btn-red btn-phone"><svg viewBox="0 0 24 24"><path fill="currentColor" d="M6.6 10.8a15 15 0 0 0 6.6 6.6l2.2-2.2a1 1 0 0 1 1-.25 11.4 11.4 0 0 0 3.6.6 1 1 0 0 1 1 1V20a1 1 0 0 1-1 1A17 17 0 0 1 3 4a1 1 0 0 1 1-1h3.5a1 1 0 0 1 1 1c0 1.25.2 2.45.6 3.6a1 1 0 0 1-.25 1z"/></svg>555-014-2288</a>
  <a class="btn btn-ghost">GET A FREE QUOTE</a>
</section>

<section class="areas">
  <div class="photo" role="img" aria-label="White double gate between tall white posts"></div>
  <h2>Our Fence &amp; Deck<br>Services Areas</h2>
  <p class="intro">The point of using Lorem Ipsum is that it has a more-or-less normal distribution of letters, as opposed to using 'Content here, content here', making it look like readable</p>
  <ul class="ticks">
    <li>Alamo Heights</li><li>San Antonio</li>
    <li>Converse</li><li>Shavano Park</li>
    <li>Castle Hills</li><li>Stone Oak</li>
    <li>Cibolo</li><li>Terrell Hills</li>
    <li>Olmos Park</li><li>Universal City</li>
  </ul>
  <p class="outro">The point of using Lorem Ipsum is that it has a more-or-less normal distribution of letters, as opposed to using</p>
  <a class="btn btn-red btn-phone"><svg viewBox="0 0 24 24"><path fill="currentColor" d="M6.6 10.8a15 15 0 0 0 6.6 6.6l2.2-2.2a1 1 0 0 1 1-.25 11.4 11.4 0 0 0 3.6.6 1 1 0 0 1 1 1V20a1 1 0 0 1-1 1A17 17 0 0 1 3 4a1 1 0 0 1 1-1h3.5a1 1 0 0 1 1 1c0 1.25.2 2.45.6 3.6a1 1 0 0 1-.25 1z"/></svg>555-014-2288</a>
  <a class="btn btn-navy">GET A FREE QUOTE</a>
</section>

<section class="testimonial">
  <div class="frame"></div>
  <div class="quote-mark">
    <svg width="50" height="42" viewBox="0 0 50 42"><path fill="#fff" d="M2 22C2 10 8 3 19 1l2 5c-6 2-9 6-9 11h9v23H2zM28 22C28 10 34 3 45 1l2 5c-6 2-9 6-9 11h9v23H28z"/></svg>
  </div>
  <div class="stars">
    <svg viewBox="0 0 24 24"><path fill="#e3161f" d="M12 2l3 6.6 7.2.8-5.4 4.9 1.5 7.1L12 17.8 5.7 21.4l1.5-7.1L1.8 9.4 9 8.6z"/></svg>
    <svg viewBox="0 0 24 24"><path fill="#e3161f" d="M12 2l3 6.6 7.2.8-5.4 4.9 1.5 7.1L12 17.8 5.7 21.4l1.5-7.1L1.8 9.4 9 8.6z"/></svg>
    <svg viewBox="0 0 24 24"><path fill="#e3161f" d="M12 2l3 6.6 7.2.8-5.4 4.9 1.5 7.1L12 17.8 5.7 21.4l1.5-7.1L1.8 9.4 9 8.6z"/></svg>
    <svg viewBox="0 0 24 24"><path fill="#e3161f" d="M12 2l3 6.6 7.2.8-5.4 4.9 1.5 7.1L12 17.8 5.7 21.4l1.5-7.1L1.8 9.4 9 8.6z"/></svg>
    <svg viewBox="0 0 24 24"><path fill="#e3161f" d="M12 2l3 6.6 7.2.8-5.4 4.9 1.5 7.1L12 17.8 5.7 21.4l1.5-7.1L1.8 9.4 9 8.6z"/></svg>
  </div>
  <span class="t-arrow prev"></span>
  <blockquote>The point of using Lorem Ipsum is that it has a more-or-less normal distribution of letters, as opposed to using 'Content here, content here', making it look like readable English. Many desktop publishing packages and web page editors now use Lorem Ipsum as their default model text,</blockquote>
  <cite>Marlow T. Benning</cite>
  <span class="role">Verified Clients</span>
  <span class="t-arrow next"></span>
</section>

<section class="faq">
  <h2>Frequently Asked Questions</h2>
  <div class="faq-item" style="left:167px;top:134px"><div class="q"><span>1. How much does fence installation cost?</span><span>+</span></div></div>
  <div class="faq-item" style="left:167px;top:187px"><div class="q"><span>2. Are you a gate company in San Antonio, Texas?</span><span>+</span></div></div>
  <div class="faq-item" style="left:167px;top:250px;border:none"><div class="q"><span>3. What makes you different from another?</span><span>-</span></div>
    <p class="a">The point of using Lorem Ipsum is that it has a more-or-less normal distribution of letters, as opposed to using 'Content here, content here', making it look like readable English. Many desktop publishing packages and web page editors now use Lorem Ipsum as their default model text, and a search.</p></div>
  <div class="faq-item" style="left:609px;top:134px"><div class="q"><span>4. What type of custom fences can I get?</span><span>+</span></div></div>
  <div class="faq-item" style="left:609px;top:187px"><div class="q"><span>5. Do you need a permit to build a fence?</span><span>+</span></div></div>
  <div class="faq-item" style="left:609px;top:243px;border:none"><div class="q"><span>6. What is the tallest fence you can install?</span><span>-</span></div>
    <p class="a">The point of using Lorem Ipsum is that it has a more-or-less normal distribution of letters, as opposed to using 'Content here, content here', making it look like readable English. Many desktop publishing packages and web page editors now use Lorem Ipsum as their default model text, and a search.</p></div>
</section>

<footer class="site-footer">
  <div class="cta-card">
    <h2>Let’s get started<br>on your project today</h2>
    <a class="btn btn-red btn-phone"><svg viewBox="0 0 24 24"><path fill="currentColor" d="M6.6 10.8a15 15 0 0 0 6.6 6.6l2.2-2.2a1 1 0 0 1 1-.25 11.4 11.4 0 0 0 3.6.6 1 1 0 0 1 1 1V20a1 1 0 0 1-1 1A17 17 0 0 1 3 4a1 1 0 0 1 1-1h3.5a1 1 0 0 1 1 1c0 1.25.2 2.45.6 3.6a1 1 0 0 1-.25 1z"/></svg>555-014-2288</a>
    <a class="btn btn-navy">GET A FREE QUOTE</a>
  </div>

  <a class="footer-brand" href="#"><i></i>Yardline Works</a>
  <p class="footer-about">The point of using Lorem Ipsum is that it has a more-or-less normal distribution of letters, as opposed to using 'Content here, content here', making it look like readable English. Many desktop publishing packages and web page editors now use</p>

  <div class="footer-col" style="left:506px">
    <h4>Quick Link</h4>
    <ul><li>Home</li><li>About Us</li><li>Services</li><li>Gallery</li><li>Contact Us</li></ul>
  </div>
  <div class="footer-col" style="left:666px;top:217px">
    <h4>Our Services</h4>
    <ul><li>Residential Fencing</li><li>Commercial Fencing</li><li>Custom Decks</li><li>Pergolas &amp; Patio Covers</li><li>Wood Fencing</li><li>Chain Link Fening</li><li>Iron Fencing</li></ul>
  </div>
  <div class="footer-col contact" style="left:866px">
    <h4>Contact us</h4>
    <ul>
      <li><svg viewBox="0 0 24 24"><path fill="currentColor" d="M12 2a7 7 0 0 0-7 7c0 5 7 13 7 13s7-8 7-13a7 7 0 0 0-7-7zm0 9.5A2.5 2.5 0 1 1 12 6.5a2.5 2.5 0 0 1 0 5z"/></svg><span>2750 Brackenfield Road,<br>Orchard Bay, FL 30418</span></li>
      <li><svg viewBox="0 0 24 24"><path fill="currentColor" d="M3 5h18v14H3zm2 2v.5l7 4.5 7-4.5V7l-7 4.5z"/></svg><span>info@yardlineworks.example</span></li>
      <li><svg viewBox="0 0 24 24"><path fill="currentColor" d="M6.6 10.8a15 15 0 0 0 6.6 6.6l2.2-2.2a1 1 0 0 1 1-.25 11.4 11.4 0 0 0 3.6.6 1 1 0 0 1 1 1V20a1 1 0 0 1-1 1A17 17 0 0 1 3 4a1 1 0 0 1 1-1h3.5a1 1 0 0 1 1 1c0 1.25.2 2.45.6 3.6a1 1 0 0 1-.25 1z"/></svg><span>555-014-2288</span></li>
    </ul>
  </div>
  <div class="socials" aria-label="Social media links">
    <span></span><span></span><span></span>
  </div>
  <div class="footer-rule"></div>
  <p class="copyright">© 2025 yardlineworks.example. All Rights Reserved</p>
</footer>

</body>
</html>
```